graphic design for a signs in automotive shop reception area

I am after a graphic design for 5 signs sized 500mm wide and 800mm high. These 5 signs will go on the wall behind the reception desk in our automotive workshop office area. The signs will display what jobs we do and prices, etc. <br/><br/>I have attached the rough layout and wording of each of the signs in the uploaded files section. Each sign is numbered in the file name. 1-5. <br/>I have also attached an example of a design i really like. If sign 1 could be very very similar to example uploaded. Can you please have a symbol in front of each listing on sign 1 like they have in the example. <br/>Vehicle Servicing (Oil symbol)<br/>All Mechanical Repairs (Spanner symbol)<br/>Warrant of Fitness (Pass/tick symbol)<br/>Tyres & Wheel Alignments (tyre symbol)<br/>Automotive Diagnostics (computer/tablet symbol)<br/>Automotive Parts & Supplies (car part symbol)<br/><br/>Can sign 2, 3 and 4 be much the same as eachother. <br/>Sign 5 can be different but basic and easy to read because of all the wording.<br/><br/>Colours are white, red and black.<br/>Company logo attached.<br/><br/>Company details:<br/>Phone: 07 342 9181<br/>Email: office@tallwheelmotors.co.nz<br/>Website: www.tallwheelmotors.co.nz <br/>

```html
<!DOCTYPE html>
<html lang="en">
<head>
<meta charset="utf-8">
<title>Tall Wheel Motors – Services Sign</title>
<link rel="stylesheet" href="https://fonts.googleapis.com/css2?family=Archivo:wght@600;700;800&family=Ubuntu:wght@400;500&display=swap">
<style>
  :root {
    --backdrop: #231f20;
    --black: #000000;
    --charcoal: #1a1a1a;
    --red: #e0212f;
    --red-bright: #ea1c24;
    --red-deep: #ad162b;
    --red-shade: #7d0f1e;
    --white: #ffffff;
    --grey-light: #d5d8dc;
    --ink: #111111;
  }
  html, body {
    margin: 0;
    padding: 0;
    width: 1200px;
    height: 1200px;
    overflow: hidden;
    background: var(--backdrop);
  }
  .sign {
    position: absolute;
    left: 289px;
    top: 101px;
    width: 623px;
    height: 998px;
    box-shadow: 0 24px 30px rgba(0,0,0,0.45);
  }
  .sign svg { display: block; width: 100%; height: 100%; }
  .service-label {
    font-family: "Archivo", Arial, sans-serif;
    font-weight: 700;
    font-size: 34px;
    fill: var(--white);
  }
  .brand-name {
    font-family: "Archivo", Arial, sans-serif;
    font-weight: 800;
    font-size: 64px;
    fill: var(--red);
  }
  .phone {
    font-family: "Archivo", Arial, sans-serif;
    font-weight: 700;
    font-size: 60px;
    fill: var(--red);
  }
  .email {
    font-family: "Ubuntu", Arial, sans-serif;
    font-weight: 500;
    font-size: 32px;
    fill: var(--ink);
  }
  .website {
    font-family: "Ubuntu", Arial, sans-serif;
    font-weight: 500;
    font-size: 40px;
    letter-spacing: 2px;
    fill: var(--white);
  }
</style>
</head>
<body>
<div class="sign">
  <svg viewBox="0 0 1003 1607" xmlns="http://www.w3.org/2000/svg">
    <defs>
      <linearGradient id="panel-bg" x1="0" y1="0" x2="0" y2="1">
        <stop offset="0" stop-color="var(--black)"/>
        <stop offset="0.8" stop-color="var(--charcoal)"/>
      </linearGradient>
      <linearGradient id="hex-fill" x1="0" y1="0" x2="1" y2="1">
        <stop offset="0" stop-color="#e3293a"/>
        <stop offset="1" stop-color="var(--red-deep)"/>
      </linearGradient>
      <radialGradient id="contact-bg" cx="0.5" cy="0.35" r="0.6">
        <stop offset="0" stop-color="var(--white)"/>
        <stop offset="1" stop-color="var(--grey-light)"/>
      </radialGradient>
      <linearGradient id="footer-bar" x1="0" y1="0" x2="1" y2="0">
        <stop offset="0" stop-color="#9e1b24"/>
        <stop offset="0.55" stop-color="var(--red-bright)"/>
        <stop offset="1" stop-color="#9e1b24"/>
      </linearGradient>
      <symbol id="hex" viewBox="0 0 148 170">
        <polygon points="74,0 148,42.5 148,127.5 74,170 0,127.5 0,42.5" fill="url(#hex-fill)"/>
        <polygon points="148,42.5 148,127.5 74,170 40,150 120,40" fill="var(--red-shade)" opacity="0.55"/>
      </symbol>
    </defs>

    <rect class="panel" width="1003" height="1607" fill="url(#panel-bg)"/>

    <!-- Service list -->
    <g class="service service--servicing" transform="translate(185 92)">
      <use href="#hex" width="148" height="170"/>
      <path d="M74 35 C64 58 46 80 46 100 a28 28 0 0 0 56 0 C102 80 84 58 74 35Z" fill="var(--white)"/>
      <path d="M60 98 a14 14 0 0 0 12 22" stroke="url(#hex-fill)" stroke-width="5" fill="none" stroke-linecap="round"/>
    </g>
    <text class="service-label" x="361" y="189">VEHICLE SERVICING</text>

    <g class="service service--repairs" transform="translate(258 232)">
      <use href="#hex" width="148" height="170"/>
      <g fill="none" stroke="var(--white)" stroke-linecap="round">
        <line x1="42" y1="118" x2="92" y2="68" stroke-width="12"/>
      </g>
      <path d="M88 56 a18 18 0 0 1 24 -12 l-10 12 4 10 10 2 10 -10 a18 18 0 0 1 -26 22Z" fill="var(--white)"/>
      <circle cx="42" cy="118" r="3.5" fill="var(--red-deep)"/>
    </g>
    <text class="service-label" x="422" y="329">ALL MECHANICAL REPAIRS</text>

    <g class="service service--wof" transform="translate(177 372)">
      <use href="#hex" width="148" height="170"/>
      <rect x="41" y="53" width="64" height="64" rx="12" fill="none" stroke="var(--white)" stroke-width="10"/>
      <path d="M55 85 l17 17 38 -52" fill="none" stroke="var(--white)" stroke-width="11" stroke-linecap="round" stroke-linejoin="round"/>
    </g>
    <text class="service-label" x="348" y="468">WARRANT OF FITNESS</text>

    <g class="service service--tyres" transform="translate(255 511)">
      <use href="#hex" width="148" height="170"/>
      <circle cx="74" cy="85" r="48" fill="var(--white)"/>
      <circle cx="74" cy="85" r="29" fill="none" stroke="var(--red)" stroke-width="7"/>
      <g stroke="var(--red)" stroke-width="6" stroke-linecap="round">
        <line x1="74" y1="85" x2="74" y2="60"/>
        <line x1="74" y1="85" x2="98" y2="78"/>
        <line x1="74" y1="85" x2="89" y2="106"/>
        <line x1="74" y1="85" x2="59" y2="106"/>
        <line x1="74" y1="85" x2="50" y2="78"/>
      </g>
      <circle cx="74" cy="85" r="6" fill="var(--white)"/>
    </g>
    <text class="service-label" x="426" y="608">TYRES &amp; WHEEL ALIGNMENTS</text>

    <g class="service service--diagnostics" transform="translate(178 650)">
      <use href="#hex" width="148" height="170"/>
      <rect x="47" y="47" width="54" height="76" rx="5" fill="none" stroke="var(--white)" stroke-width="5"/>
      <circle cx="74" cy="116" r="3" fill="var(--white)"/>
    </g>
    <text class="service-label" x="352" y="747">AUTOMOTIVE DIAGNOSTICS</text>

    <g class="service service--parts" transform="translate(102 790)">
      <use href="#hex" width="148" height="170"/>
      <g transform="rotate(45 74 85)" fill="var(--white)">
        <rect x="68" y="30" width="12" height="16"/>
        <rect x="62" y="46" width="24" height="30" rx="3"/>
        <rect x="64" y="78" width="20" height="22"/>
        <rect x="70" y="100" width="8" height="18"/>
        <rect x="65" y="118" width="10" height="4"/>
      </g>
    </g>
    <text class="service-label" x="273" y="887">AUTOMOTIVE PARTS &amp; SUPPLIES</text>

    <!-- Angled red bands -->
    <polygon class="band band--light" points="0,1070 383,1140 0,1257" fill="var(--red)"/>
    <polygon class="band band--deep" points="1003,954 1003,1073 0,1277 0,1257 383,1140" fill="var(--red-deep)"/>

    <!-- Contact area -->
    <polygon class="contact-panel" points="0,1277 1003,1073 1003,1515 0,1515" fill="url(#contact-bg)"/>

    <text class="brand-name" x="501" y="1336" text-anchor="middle">TALL WHEEL MOTORS</text>

    <g class="phone-icon" transform="translate(305 1407)">
      <rect x="0" y="0" width="22" height="40" rx="3" fill="var(--red)"/>
      <rect x="4" y="5" width="14" height="28" fill="var(--white)"/>
    </g>
    <text class="phone" x="341" y="1447">07 342 9181</text>
    <text class="email" x="501" y="1487" text-anchor="middle">office@tallwheelmotors.co.nz</text>

    <rect class="footer-bar" x="0" y="1514" width="1003" height="93" fill="url(#footer-bar)"/>
    <text class="website" x="501" y="1571" text-anchor="middle">www.tallwheelmotors.co.nz</text>
  </svg>
</div>
</body>
</html>
```